Banner 34"x81"

This is for a Pull Up Banner
I am supplying a sample of my logo and some of my art work for you to incorporate into an upright banner.
Please business name:LuellaRo OpenHarbor Psychotherapy
phone number: 583-214-9067 NOT THE ONE ON THE BUSINESS CARD

```html
<!DOCTYPE html>
<html lang="en">
<head>
<meta charset="utf-8">
<title>LuellaRo OpenHarbor Psychotherapy – Pull Up Banner</title>
<link rel="stylesheet" href="https://fonts.googleapis.com/css2?family=Poppins:wght@300;700&family=Oswald:wght@300;400&display=swap">
<style>
  :root {
    --navy: #213f91;
    --mark-blue: #1f5aa8;
    --white: #ffffff;
    --gold-light: #f0cd45;
    --gold-mid: #d9a91c;
    --gold-fade: rgba(217, 169, 28, 0);
    --photo-dark: #2b1c18;
    --photo-blue: #1357d6;
  }
  html, body {
    margin: 0;
    padding: 0;
    overflow: hidden;
    background: var(--navy);
  }
  .banner {
    position: relative;
    width: 1200px;
    height: 2859px;
    background: var(--navy);
    overflow: hidden;
    color: var(--white);
  }
  .gold-wash {
    position: absolute;
  }
  .gold-wash-top {
    left: 0;
    top: 0;
    width: 900px;
    height: 600px;
    background: radial-gradient(ellipse 100% 100% at 0 0, var(--gold-mid) 0%, var(--gold-light) 55%, var(--gold-fade) 100%);
  }
  .gold-wash-bottom {
    right: 0;
    bottom: 0;
    width: 560px;
    height: 320px;
    background: radial-gradient(ellipse 100% 100% at 100% 100%, var(--gold-mid) 0%, var(--gold-light) 55%, var(--gold-fade) 100%);
  }
  .portrait-frame {
    position: absolute;
    left: 0;
    top: 0;
    width: 1200px;
    height: 1000px;
  }
  .portrait {
    position: absolute;
    left: 428px;
    top: 425px;
    width: 342px;
    height: 513px;
    background: linear-gradient(180deg, var(--photo-dark) 0%, #3a2620 35%, var(--photo-blue) 60%, #6d6b74 85%, var(--photo-dark) 100%);
  }
  .practice-name {
    position: absolute;
    left: 0;
    width: 1200px;
    text-align: center;
    margin: 0;
    line-height: 1;
  }
  .practice-place {
    top: 1062px;
    font-family: "Poppins", sans-serif;
    font-weight: 300;
    font-size: 112px;
    letter-spacing: -1px;
  }
  .practice-owner {
    top: 1174px;
    font-family: "Poppins", sans-serif;
    font-weight: 700;
    font-size: 162px;
    letter-spacing: -3px;
  }
  .practice-field {
    top: 1378px;
    font-family: "Oswald", sans-serif;
    font-weight: 400;
    font-size: 72px;
    letter-spacing: 36px;
    padding-left: 36px;
    box-sizing: border-box;
  }
  .brand-block {
    position: absolute;
    left: 305px;
    top: 1552px;
    width: 592px;
    height: 483px;
    background: var(--mark-blue);
    display: flex;
    align-items: center;
    justify-content: center;
    font-family: "Poppins", sans-serif;
    font-weight: 700;
    font-size: 96px;
    color: var(--white);
  }
  .contact {
    position: absolute;
    left: 0;
    width: 1200px;
    height: 90px;
  }
  .contact-icon {
    position: absolute;
    left: 296px;
  }
  .contact-text {
    position: absolute;
    left: 396px;
    margin: 0;
    line-height: 1;
    white-space: nowrap;
  }
  .contact-phone { top: 2123px; height: 100px; }
  .contact-phone .contact-icon { left: 303px; top: 0; }
  .contact-phone .contact-text {
    top: 6px;
    font-family: "Poppins", sans-serif;
    font-weight: 700;
    font-size: 86px;
    letter-spacing: 1px;
  }
  .contact-line .contact-icon { top: 0; }
  .contact-line .contact-text {
    top: 2px;
    font-family: "Oswald", sans-serif;
    font-weight: 300;
    font-size: 60px;
  }
  .contact-email { top: 2261px; }
  .contact-page { top: 2366px; }
  .contact-feed { top: 2474px; }
</style>
</head>
<body>
<div class="banner">

  <div class="gold-wash gold-wash-top" role="img" aria-label="Textured gold paint splash in the top left corner"></div>
  <div class="gold-wash gold-wash-bottom" role="img" aria-label="Textured gold paint splash in the bottom right corner"></div>

  <svg class="portrait-frame" viewBox="0 0 1200 1000" aria-hidden="true">
    <path d="M494 389 H399 V974 H800 V461" fill="none" stroke="var(--white)" stroke-width="28"/>
  </svg>
  <div class="portrait" role="img" aria-label="Portrait of the therapist seated on a dark leather sofa"></div>

  <h1 class="practice-name practice-place">OpenHarbor</h1>
  <p class="practice-name practice-owner">LuellaRo</p>
  <p class="practice-name practice-field">PSYCHOTHERAPY</p>

  <div class="brand-block">LuellaRo</div>

  <div class="contact contact-phone">
    <svg class="contact-icon" width="56" height="100" viewBox="0 0 56 100" aria-hidden="true">
      <rect x="3" y="3" width="50" height="94" rx="8" fill="none" stroke="var(--white)" stroke-width="6"/>
      <line x1="3" y1="18" x2="53" y2="18" stroke="var(--white)" stroke-width="5"/>
      <line x1="3" y1="80" x2="53" y2="80" stroke="var(--white)" stroke-width="5"/>
      <circle cx="28" cy="89" r="3.5" fill="var(--white)"/>
      <path d="M18 36 C15 44 22 60 34 64 L39 60 L33 54 L30 56 C26 53 23 48 23 44 L26 42 L22 34 Z" fill="var(--white)"/>
    </svg>
    <p class="contact-text">583-214-9067</p>
  </div>

  <div class="contact contact-line contact-email">
    <svg class="contact-icon" width="74" height="74" viewBox="0 0 74 74" aria-hidden="true">
      <circle cx="37" cy="37" r="37" fill="var(--white)"/>
      <rect x="17" y="24" width="40" height="27" rx="3" fill="none" stroke="var(--navy)" stroke-width="4"/>
      <path d="M18 26 L37 41 L56 26 M18 50 L31 37 M56 50 L43 37" fill="none" stroke="var(--navy)" stroke-width="3.5"/>
    </svg>
    <p class="contact-text">LuellaOpenHarbor@harbormail.com</p>
  </div>

  <div class="contact contact-line contact-page">
    <svg class="contact-icon" width="74" height="74" viewBox="0 0 74 74" aria-hidden="true">
      <circle cx="37" cy="37" r="35" fill="var(--white)"/>
    </svg>
    <p class="contact-text">@LuellaOpenHarbour</p>
  </div>

  <div class="contact contact-line contact-feed">
    <svg class="contact-icon" width="74" height="74" viewBox="0 0 74 74" aria-hidden="true">
      <circle cx="37" cy="37" r="37" fill="var(--white)"/>
    </svg>
    <p class="contact-text">@LuellaHarbor</p>
  </div>

</div>
</body>
</html>
```